Northern Terrain Published Photographer Website

I need a website to feature a home page slide show of 6 of my top photos then a few simple pages including; gallery, bio, social, checkout, services
Updates

Need extra days to review

Target Market(s)

photography

Industry/Entity Type

Photographer

Coding

Coded - Design and coding required

Number of Pages Required

5+ page

Colors

Designer to choose colors to be used in the design.

Requirements
Must have
• clean eye catching elegant trendy
Nice to have
• unique and creative from other photographer websites

```html
<!DOCTYPE html>
<html lang="en">
<head>
<meta charset="utf-8">
<title>Maren Holloway Photography</title>
<link href="https://fonts.googleapis.com/css2?family=Playball&family=Lato:wght@400;700&family=Lora:ital@1&family=Montserrat:wght@500&display=swap" rel="stylesheet">
<style>
:root{
  --green:#8cc43c;
  --ink:#111111;
  --muted:#8a8a8a;
  --nav:#777777;
  --soft:#f7f7f7;
  --line:#d9d9d9;
}
*{margin:0;padding:0;box-sizing:border-box}
html,body{width:1200px;height:4271px;overflow:hidden;background:#fff}
body{position:relative;font-family:"Lato",sans-serif;color:var(--ink)}
.abs{position:absolute}
.photo{position:absolute}
.brand{left:78px;top:36px;font-family:"Lato",sans-serif;font-size:26px;color:var(--green);display:flex;align-items:center;gap:10px}
.brand-dot{width:16px;height:16px;border-radius:50%;background:var(--green)}
.nav{top:40px;font-size:16px;color:var(--nav)}
.nav.active{color:var(--green);font-weight:700}
.nav-caret{left:455px;top:72px;width:0;height:0;border-left:6px solid transparent;border-right:6px solid transparent;border-bottom:9px solid var(--green)}
.search{left:1070px;top:31px;width:52px;height:52px;background:var(--green);display:flex;align-items:center;justify-content:center}
.heading{left:0;width:1200px;text-align:center;font-family:"Playball",cursive;font-size:70px;line-height:1;color:var(--ink)}
.lead{left:300px;width:600px;text-align:center;font-size:15px;line-height:27px;color:var(--muted)}
.btn{background:var(--green);color:#fff;font-family:"Lato",sans-serif;font-weight:700;font-size:15px;border-radius:30px;display:flex;align-items:center;justify-content:center}
.about-sub{left:78px;top:1164px;font-family:"Montserrat",sans-serif;font-weight:500;font-size:27px}
.about-copy{left:78px;width:520px;font-size:14px;line-height:26px;color:var(--muted)}
.service{position:absolute;top:2853px;width:192px;height:320px;border:1px solid var(--line);background:#fff}
.service .photo{left:0;top:0;width:190px;height:257px}
.service-label{position:absolute;left:0;top:262px;width:190px;text-align:center;font-family:"Lora",serif;font-style:italic;font-size:24px;color:var(--green)}
.post-title{font-family:"Lora",serif;font-style:italic;font-size:21px;line-height:30px;color:var(--green)}
.post-date{font-size:13px;color:#333}
.post-copy{font-size:14px;line-height:26px;color:var(--muted)}
.feature-text{color:#fff}
.social-band{left:0;top:3869px;width:1200px;height:340px;background:var(--soft)}
.handle{left:0;width:1200px;top:4046px;text-align:center;font-family:"Playball",cursive;font-size:48px}
.footer{left:0;top:4209px;width:1200px;height:62px;background:var(--green);color:#fff;font-size:13px;display:flex;align-items:center;justify-content:center}
</style>
</head>
<body>

<header>
  <div class="abs brand"><span>Maren Holloway</span><span class="brand-dot"></span></div>
  <span class="abs nav active" style="left:437px">Home</span>
  <span class="abs nav-caret"></span>
  <span class="abs nav" style="left:522px">Bio</span>
  <span class="abs nav" style="left:583px">Services</span>
  <span class="abs nav" style="left:683px">Gallery</span>
  <span class="abs nav" style="left:777px">Social</span>
  <span class="abs nav" style="left:855px">Checkout</span>
  <span class="abs nav" style="left:964px">Contact</span>
  <div class="abs search">
    <svg width="22" height="22" viewBox="0 0 22 22"><circle cx="9" cy="9" r="7" fill="none" stroke="#fff" stroke-width="2"/><line x1="14" y1="14" x2="20" y2="20" stroke="#fff" stroke-width="2"/></svg>
  </div>
</header>

<section class="hero">
  <h1 class="abs heading" style="top:152px">Creative Photography</h1>
  <p class="abs lead" style="top:245px">Lorem ipsum dolor sit amet, consectetur adipiscing elit, sed do eiusmod tempor incididunt ut labore et dolore magna aliqua.</p>
  <a class="abs btn" style="left:522px;top:325px;width:156px;height:50px">SEE MY WORK</a>

  <div class="photo" role="img" aria-label="Moon over a dark lake at night" style="left:27px;top:620px;width:199px;height:197px;background:linear-gradient(#1d3361,#0f1d3a 60%,#05080f)"></div>
  <div class="photo" role="img" aria-label="Lighthouse silhouette at orange sunset" style="left:245px;top:437px;width:418px;height:259px;background:linear-gradient(#e84a10,#f47a18 55%,#2a0c04 80%)"></div>
  <div class="photo" role="img" aria-label="Elk standing in a grassy field" style="left:683px;top:510px;width:187px;height:186px;background:linear-gradient(#8ea560,#7a7a3e 60%,#6e6a45)"></div>
  <div class="photo" role="img" aria-label="Butterfly on purple wildflowers" style="left:245px;top:718px;width:187px;height:187px;background:linear-gradient(135deg,#6d8f35,#a877b8 50%,#d8c430)"></div>
  <div class="photo" role="img" aria-label="Monarch butterfly on white hydrangea" style="left:454px;top:718px;width:416px;height:260px;background:radial-gradient(circle at 50% 50%,#f5e6d2,#e6c7a0 45%,#3f6d2a 80%)"></div>
  <div class="photo" role="img" aria-label="Moon rising behind desert trees at dusk" style="left:891px;top:578px;width:282px;height:280px;background:linear-gradient(#3a1a5a,#c2387a 65%,#2a0d3a)"></div>
</section>

<section class="about">
  <h2 class="abs heading" style="top:1050px">About Maren Holloway</h2>
  <h3 class="abs about-sub">Lorem ipsum dolor sit am consectetur.</h3>
  <p class="abs about-copy" style="top:1213px">Lorem ipsum dolor sit amet, consectetur adipiscing elit, sed do eiusmod tempor incididunt ut labore et dolore magna aliqua. Ut enim ad minim veniam, quis nostrud exercitation ullamco laboris nisi ut aliquip ex ea commodo consequat. Duis aute irure dolor in reprehenderit in voluptate velit esse cillum dolore eu fugiat nulla pariatur. Excepteur sint occaecat cupidatat non proident, sunt in culpa qui officia deserunt mollit anim id est laborum.</p>
  <p class="abs about-copy" style="top:1390px">Lorem ipsum dolor sit amet, consectetur adipiscing elit, sed do eiusmod tempor incididunt ut labore et dolore magna aliqua. Ut enim ad minim veniam, quis nostrud exercitation ullamco laboris nisi ut aliquip ex ea commodo consequat. Duis aute irure dolor in reprehenderit in voluptate velit esse cillum dolore eu fugiat nulla pariatur. Excepteur sint occaecat cupidatat non proident, sunt in culpa qui officia deserunt mollit anim id est laborum.</p>
  <a class="abs btn" style="left:78px;top:1584px;width:154px;height:50px">READ MORE</a>

  <div class="photo" role="img" aria-label="Wooden pier leading out over the sea" style="left:727px;top:1166px;width:394px;height:414px;background:linear-gradient(#dcebf3,#a9cde0 40%,#7d6a55 75%,#5a4a3a)"></div>
  <div class="photo" role="img" aria-label="Photographer seated on the bow of a boat" style="left:655px;top:1218px;width:394px;height:416px;background:linear-gradient(#354556,#48596a 45%,#c9ccd0 70%,#eeeeee)"></div>
</section>

<section class="gallery">
  <h2 class="abs heading" style="top:1716px">Work Gallery</h2>
  <p class="abs lead" style="top:1806px">Lorem ipsum dolor sit amet, consectetur adipiscing elit, sed do eiusmod tempor incididunt ut labore et dolore magna aliqua.</p>

  <div class="photo" role="img" aria-label="Canyon under storm clouds" style="left:0;top:1905px;width:207px;height:351px;background:linear-gradient(#3b6ea8,#c88a5a 40%,#7a3a20 70%,#3a2018)"></div>
  <div class="photo" role="img" aria-label="Figure on a pier at red sunset" style="left:229px;top:1998px;width:364px;height:259px;background:linear-gradient(#c4300c,#f0561a 55%,#2a0804)"></div>
  <div class="photo" role="img" aria-label="Purple dusk over water" style="left:615px;top:1977px;width:124px;height:104px;background:linear-gradient(#221a55,#b8302a 60%,#120818)"></div>
  <div class="photo" role="img" aria-label="Red rock formation under blue sky" style="left:761px;top:1915px;width:124px;height:166px;background:linear-gradient(#3f86d4,#c2663a 45%,#7a3a1c)"></div>
  <div class="photo" role="img" aria-label="Sun setting behind desert rocks" style="left:906px;top:1967px;width:187px;height:187px;background:linear-gradient(#2f6fb8,#f0c030 50%,#3a2010 80%)"></div>
  <div class="photo" role="img" aria-label="Sunset through trees by a lake" style="left:615px;top:2103px;width:270px;height:280px;background:radial-gradient(circle at 50% 45%,#ffd24a,#e0801a 35%,#2a1a08 80%)"></div>
  <div class="photo" role="img" aria-label="Pier posts at golden sunrise" style="left:906px;top:2176px;width:187px;height:187px;background:linear-gradient(#3a1e08,#f0a020 40%,#6a3a10 75%,#1a0e04)"></div>
  <div class="photo" role="img" aria-label="Sunset over a waterfront" style="left:1113px;top:1967px;width:87px;height:519px;background:linear-gradient(#3a4a6a,#f0a030 45%,#8a4010 75%,#2a1006)"></div>
  <div class="photo" role="img" aria-label="Desert tree against pink sky" style="left:0;top:2280px;width:312px;height:311px;background:linear-gradient(#8a3a8a,#e05a6a 45%,#4a1a4a 80%)"></div>
  <div class="photo" role="img" aria-label="Sun through forest over mountains" style="left:333px;top:2280px;width:260px;height:186px;background:linear-gradient(#6f9ad0,#e8eef5 30%,#3a4e6a 65%,#5a4a2a)"></div>
</section>

<section class="services">
  <h2 class="abs heading" style="top:2674px">Our Services</h2>
  <p class="abs lead" style="top:2764px">Lorem ipsum dolor sit amet, consectetur adipiscing elit, sed do eiusmod tempor incididunt ut labore et dolore magna aliqua.</p>

  <div class="service" style="left:78px">
    <div class="photo" role="img" aria-label="Waterfall beneath a rail bridge" style="background:linear-gradient(#dfe8ea,#8aa05a 45%,#e8eef0 70%,#5a6a3a)"></div>
    <div class="service-label">Nature</div>
  </div>
  <div class="service" style="left:292px">
    <div class="photo" role="img" aria-label="Glass sphere among red rocks" style="background:linear-gradient(#b8501a,#e0b08a 35%,#c8783a 65%,#7a3012)"></div>
    <div class="service-label">Landscape</div>
  </div>
  <div class="service" style="left:505px">
    <div class="photo" role="img" aria-label="Elk in a meadow" style="background:linear-gradient(#9aae6a,#7a6a40 55%,#6a7a3a)"></div>
    <div class="service-label">Wildlife</div>
  </div>
  <div class="service" style="left:717px">
    <div class="photo" role="img" aria-label="Sunburst under a rock arch" style="background:linear-gradient(#2a64c0,#5a8ad8 35%,#7a4a30 55%,#c89070 80%)"></div>
    <div class="service-label">Sunsets</div>
  </div>
  <div class="service" style="left:931px">
    <div class="photo" role="img" aria-label="Pier at orange sunrise" style="background:linear-gradient(#e06010,#f8b020 40%,#c06010 70%,#3a1a06)"></div>
    <div class="service-label">Sunrises</div>
  </div>
</section>

<section class="blog">
  <h2 class="abs heading" style="top:3259px">Our Creative Blog</h2>
  <p class="abs lead" style="top:3347px">Lorem ipsum dolor sit amet, consectetur adipiscing elit, sed do eiusmod tempor incididunt ut labore et dolore magna aliqua.</p>

  <article>
    <div class="photo" role="img" aria-label="Dusk sky over a harbour" style="left:78px;top:3437px;width:499px;height:393px;background:linear-gradient(#3a3220,#8a5a30 45%,#6a3a20 75%,#1a1208)"></div>
    <div class="abs feature-text" style="left:101px;top:3660px;width:440px">
      <div class="post-title" style="color:#fff">Lorem ipsum dolor sit amet,adipiscing elit.</div>
      <div class="post-date" style="color:#fff;margin-top:10px">29 May 2019</div>
      <div class="post-copy" style="color:#fff;margin-top:8px">Lorem ipsum dolor sit amet, consectetur adipiscing elit, sed do eiusmod tempor incididunt ut labore et dolore magna.</div>
    </div>
  </article>

  <article>
    <div class="photo" role="img" aria-label="Falls beside a city skyline" style="left:598px;top:3437px;width:207px;height:187px;background:linear-gradient(#5a8ad0,#b0c8e8 40%,#e8eef2 65%,#4a4a4a)"></div>
    <div class="abs" style="left:838px;top:3435px;width:300px">
      <div class="post-title">Lorem ipsum dolor sit amet, consectetur adipiscing elit.</div>
      <div class="post-date" style="margin-top:8px">29 May 2019</div>
      <div class="post-copy" style="margin-top:6px">Lorem ipsum dolor sit amet, consectetur adipiscing elit, sed do eiusmod tempor incididunt ut labore et dolore magna.</div>
    </div>
  </article>

  <article>
    <div class="photo" role="img" aria-label="Street sign among palm trees" style="left:598px;top:3644px;width:207px;height:186px;background:linear-gradient(#4a8ae0,#a8c8f0 45%,#3a5a2a 75%,#5a6a4a)"></div>
    <div class="abs" style="left:838px;top:3642px;width:300px">
      <div class="post-title">Lorem ipsum dolor sit amet, consectetur adipiscing elit.</div>
      <div class="post-date" style="margin-top:8px">29 May 2019</div>
      <div class="post-copy" style="margin-top:6px">Lorem ipsum dolor sit amet, consectetur adipiscing elit, sed do eiusmod tempor incididunt ut labore et dolore magna.</div>
    </div>
  </article>
</section>

<section class="social">
  <div class="abs social-band"></div>
  <div class="photo" role="img" aria-label="Pink dusk over calm water" style="left:78px;top:3894px;width:144px;height:144px;border:6px solid var(--green);background:linear-gradient(#c86a9a,#e090a0 45%,#6a4a7a)"></div>
  <div class="photo" role="img" aria-label="Sunset behind bare trees" style="left:179px;top:4089px;width:129px;height:120px;background:linear-gradient(#2a3a6a,#f08a20 55%,#1a1008)"></div>
  <div class="abs" style="left:547px;top:3936px;width:102px;height:102px;border-radius:50%;background:linear-gradient(135deg,#f5a623,#e8336e 55%,#8a3ab9)"></div>
  <div class="abs handle">@maren.h.photography</div>
  <div class="abs" style="left:944px;top:3935px;width:229px;height:227px;border:22px solid var(--green);background:#fff"></div>
  <div class="photo" role="img" aria-label="Snowy park path with bare trees" style="left:991px;top:3982px;width:138px;height:134px;background:linear-gradient(#7aa8e0,#e8eef5 50%,#ffffff 75%,#5a5a6a)"></div>
</section>

<footer class="abs footer">Copyright ©&nbsp;<strong>Maren Holloway</strong>&nbsp;- 2019 . All Right Reserved</footer>

</body>
</html>
```